International Trading Company, 'KIRO' needs a Business Card

The company name is "KIRO" and it has own logo design.
I'd like to use its logo on this business card.
I need two side Business Card.
I'll look forward to your great design.
Thank you very much in advance.

Contact Information for Business Card

Company Name : Kiro Harbour Limited
Information Example
Dorian Pallister
Mobile(use icon please) : 1 (212) 555-0143
Tel(use icon please) : 1 (212) 555-0178
Email(use icon please) : dorian27@kiroharbour-mail.com
Address(use icon please) : 482 Halden Ave, New York, NY 10160, USA

```html
<!DOCTYPE html>
<html lang="en">
<head>
<meta charset="utf-8">
<title>Kiro Harbour Limited – Business Card</title>
<link rel="stylesheet" href="https://fonts.googleapis.com/css2?family=Arimo:wght@400;700&family=Tinos:wght@400&display=swap">
<style>
  :root {
    --backdrop: #b4b4b4;
    --card-grey: #5f5f5f;
    --card-black: #050505;
    --mark-grey: #6a6a6a;
    --ink: #0d0d0d;
    --rule: #2a2a2a;
  }
  * { margin: 0; padding: 0; box-sizing: border-box; }
  html, body { width: 1200px; height: 800px; overflow: hidden; }
  body {
    background: var(--backdrop);
    display: flex;
    align-items: center;
    justify-content: center;
    gap: 140px;
  }
  .card {
    width: 320px;
    height: 560px;
    background: var(--card-grey);
    position: relative;
    box-shadow: 0 10px 26px rgba(0,0,0,0.28);
    overflow: hidden;
  }
  /* Front */
  .front__band {
    background: var(--card-black);
    height: 132px;
    padding: 26px 22px 0;
  }
  .brand-name {
    font-family: "Arimo", sans-serif;
    font-weight: 700;
    color: var(--mark-grey);
    font-size: 64px;
    line-height: 1;
    letter-spacing: 10px;
  }
  .company-name {
    font-family: "Arimo", sans-serif;
    font-weight: 700;
    color: var(--mark-grey);
    font-size: 15.5px;
    letter-spacing: 1px;
    text-transform: uppercase;
    margin-top: 8px;
    white-space: nowrap;
  }
  .holder {
    margin: 58px 34px 0;
    padding-bottom: 8px;
    border-bottom: 1px solid var(--rule);
    font-family: "Tinos", serif;
    font-size: 22px;
    letter-spacing: 1.5px;
    color: var(--ink);
    text-transform: uppercase;
  }
  .contacts {
    position: absolute;
    left: 26px;
    right: 14px;
    bottom: 32px;
    list-style: none;
    font-family: "Tinos", serif;
    font-size: 11.5px;
    color: var(--ink);
  }
  .contacts li {
    display: flex;
    align-items: center;
    gap: 8px;
    margin-top: 5px;
    white-space: nowrap;
  }
  .contacts svg { width: 13px; height: 13px; flex: none; fill: var(--ink); }
  /* Back */
  .back__band {
    position: absolute;
    left: 0; right: 0; bottom: 0;
    height: 380px;
    background: var(--card-black);
    display: flex;
    align-items: center;
    justify-content: center;
  }
  .back .brand-name { font-size: 76px; letter-spacing: 12px; }
</style>
</head>
<body>
  <section class="card front" aria-label="Card front">
    <header class="front__band">
      <div class="brand-name">KIRO</div>
      <div class="company-name">Kiro Harbour Limited</div>
    </header>
    <h1 class="holder">Dorian Pallister</h1>
    <ul class="contacts">
      <li>
        <svg viewBox="0 0 16 16" aria-label="Address"><path d="M8 1 1 7.5h2V15h4v-4h2v4h4V7.5h2z"/></svg>
        482 Halden Ave, New York, NY 10160, USA
      </li>
      <li>
        <svg viewBox="0 0 16 16" aria-label="Mobile"><path d="M4.5 0h7A1.5 1.5 0 0 1 13 1.5v13a1.5 1.5 0 0 1-1.5 1.5h-7A1.5 1.5 0 0 1 3 14.5v-13A1.5 1.5 0 0 1 4.5 0zM5 2v10h6V2zm3 11a1 1 0 1 0 0 2 1 1 0 0 0 0-2z"/></svg>
        1 (212) 555-0143
      </li>
      <li>
        <svg viewBox="0 0 16 16" aria-label="Telephone"><path d="M3.6 1 6 3.4 4.7 5.5a9 9 0 0 0 5.8 5.8l2.1-1.3L15 12.4l-1.7 2.3C7.5 15 1 8.5 1.3 2.7z"/></svg>
        1 (212) 555-0178
      </li>
      <li>
        <svg viewBox="0 0 16 16" aria-label="Email"><path d="M0 3h16v10H0zm1.5 1.3v.3L8 9l6.5-4.4v-.3zm0 2.1V11.7h13V6.4L8 10.8z"/></svg>
        dorian27@kiroharbour-mail.com
      </li>
    </ul>
  </section>

  <section class="card back" aria-label="Card back">
    <div class="back__band">
      <div class="brand-name">KIRO</div>
    </div>
  </section>
</body>
</html>
```